blaze otto: flyer/menu board design for modern food van/trailer concept.

who are we? a modern food van/trailer selling restuarant quality food (burrito, burgers, waffles).our demographic is 16 - 35.

what do we need? a design for a flyer A4 size that is divided in 3 sections.with our menu on the inside and a design on the outside with our logo. the style must be funky, cool and modern.

Our restaurant theme is based on the movie "stone moth" by lorcan vedrassi. So any designs should be somehow linked to that genre.

the same menu on the flyer will be posted on our menu board. there is a chance we will use an lcd menu board so the format must accomodate that.
the menu must also be easilly modified in case we need to update changes pricing and menu items.

thank you
team blaze otto
Updates

Hi, Project will become non-refundable as soon as i get some good designs. Thank you and good luck Team blaze otto

Dear designers, I have uploaded some example menus, pics, my logo and hand drawings of my vision of how i would like the flyer/menu to look like. I understand that some designers cant see my uploads. I have contacted pixel harbor and they are trying to fix the issue. The deadline will be extended if needed. Thank you for your patients and your designs. Regards, Otto

Hi, To those who are having trouble viewing my uploads, here is the link http://gigs.pixelharbrio.com/job.aspx?id=519370

Target Market(s)

our target market is young and cool between the ages of16 - 35. we are a multicultural society in a western governed country. Sydney Australia.

Industry/Entity Type

Restaurant

Font styles to use
Serif

Requirements
Must have
• pictures of menu items in a hand drawn black and white style: burger, burrito, waffles, buffallo wings, chicken, beef, prawn. examples provided
please feel free to show off your alternate ideas.
style should be modern, cool and funky. examples provided
Nice to have
• Colours: yellow, red, black.
Pictures/illustrations: black & white in a sketch style.
Theme: ninja, Mexican, modern, funky.

```html
<!DOCTYPE html>
<html lang="en">
<head>
<meta charset="utf-8">
<title>Blaze Otto — Menu</title>
<link rel="stylesheet" href="https://fonts.googleapis.com/css2?family=Alfa+Slab+One&family=Amatic+SC:wght@700&family=Caveat+Brush&family=Josefin+Sans:wght@400;600&family=Roboto+Slab:wght@700;800&display=swap">
<style>
:root{
  --bg:#dfe3e3;
  --paper:#ffffff;
  --paper-grey:#eef0f0;
  --ink:#1e1e1e;
  --item:#5b5b5b;
  --red:#e8374e;
  --orange:#f06a3a;
  --yellow:#f7b515;
  --mild:#f2a65a;
  --hot:#ea3f55;
  --sketch:#cfcfcf;
}
*{box-sizing:border-box;margin:0;padding:0}
html,body{width:1200px;height:1134px;overflow:hidden;background:var(--bg)}
body{font-family:'Josefin Sans',sans-serif;color:var(--ink)}
.menu{display:flex;width:1200px;height:1134px}
.panel{width:400px;height:1134px;padding:34px 22px 28px;position:relative;display:flex;flex-direction:column}
.panel--left{background:var(--paper)}
.panel--middle{background:var(--paper-grey)}
.panel--right{background:linear-gradient(90deg,#e3e6e6,#f6f7f7 40%,#fafafa)}
.section-title{font-family:'Alfa Slab One',serif;color:var(--red);font-size:19px;letter-spacing:.5px;text-transform:uppercase;line-height:1.1}
.tagline{font-size:18px;line-height:1.25;margin-top:6px}
.head-row{display:flex;align-items:center;justify-content:space-between;gap:10px}
.sketch{background:linear-gradient(135deg,#f4f4f4,var(--sketch));border-radius:8px;flex:none}
.tag{position:relative;display:inline-flex;align-items:center;justify-content:center;width:86px;height:44px;flex:none;transform:rotate(-6deg)}
.tag svg{position:absolute;inset:0;width:100%;height:100%}
.tag span{position:relative;font-family:'Caveat Brush',cursive;font-size:27px;padding-left:14px}
.tag--small{width:74px;height:40px}
.tag--small span{font-size:24px}
.step{display:flex;align-items:center;height:50px;margin:16px -22px 14px;padding-left:22px;
  background:linear-gradient(90deg,var(--yellow) 0,var(--orange) 35%,var(--red) 70%,rgba(232,55,78,0) 100%)}
.step-label{font-family:'Roboto Slab',serif;font-weight:800;font-size:20px;line-height:.9;text-transform:uppercase;width:70px}
.step-title{font-family:'Amatic SC',sans-serif;font-size:35px;color:#fff;letter-spacing:1px;text-transform:uppercase}
.item{margin-bottom:9px}
.item-name{font-family:'Alfa Slab One',serif;font-size:16px;color:var(--item);letter-spacing:1px;text-transform:uppercase;line-height:1.15}
.item-desc{font-size:13.5px;line-height:1.3}
.leader{display:flex;align-items:baseline;margin-bottom:10px;font-size:13.5px}
.leader .item-name{flex:none}
.leader .dots{flex:1;border-bottom:2px dotted #777;margin:0 3px;transform:translateY(-4px)}
.leader .value{flex:none}
.heat{font-family:'Alfa Slab One',serif;font-size:15px}
.heat--mild{color:var(--mild)}
.heat--medium{color:#f07a4f}
.heat--hot,.heat--insane{color:var(--hot)}
.fillings-art{display:flex;justify-content:space-between;margin:6px 4px 14px}
.fillings-art .sketch{width:78px;height:58px;border-radius:40%}
.meal{display:flex;align-items:center;justify-content:space-between;margin-top:auto}
.meal .section-title{font-size:18px}
.meal-desc{font-size:15px;margin-top:2px}
.spacer{height:14px}
.price-row{display:flex;justify-content:space-between;align-items:flex-start;margin:6px 0 40px}
.pack{display:flex;flex-direction:column;align-items:center;font-size:14px}
.pack .tag{margin-top:4px}
.notice{margin-top:auto;border:4px solid;border-image:linear-gradient(135deg,var(--yellow),var(--red),var(--yellow)) 1;
  background:#fff;padding:22px 30px 20px;text-align:center;font-family:'Roboto Slab',serif;font-weight:700;font-size:15px;line-height:1.3;position:relative}
.notice p+p{margin-top:12px}
.chili{position:absolute;bottom:14px;width:22px;height:56px;background:linear-gradient(#f7c55a,#ef7b3d);border-radius:50% 50% 50% 50%/30% 30% 70% 70%}
.chili--left{left:10px;transform:rotate(-20deg)}
.chili--right{right:10px;transform:rotate(20deg)}
</style>
</head>
<body>
<main class="menu">

  <!-- Burritos -->
  <section class="panel panel--left">
    <div class="head-row">
      <div>
        <h2 class="section-title">Burritos</h2>
        <p class="tagline">What is a burrito?<br>A Mexican kebab, mate!</p>
      </div>
      <div class="sketch" style="width:96px;height:70px" role="img" aria-label="Hand-drawn sketch of a burrito"></div>
      <div class="tag"><svg viewBox="0 0 100 50" preserveAspectRatio="none"><path d="M3 25 L20 4 H97 V46 H20 Z" fill="#fff" stroke="#1e1e1e" stroke-width="2.5"/><circle cx="16" cy="25" r="3" fill="none" stroke="#1e1e1e" stroke-width="2"/></svg><span>$9</span></div>
    </div>

    <div class="step"><span class="step-label">Step One</span><span class="step-title">Choose your style</span></div>
    <div class="item"><div class="item-name">Original</div><div class="item-desc">Lettuce, Salsa, Guacamole &amp; Sour Cream</div></div>
    <div class="item"><div class="item-name">Fajita</div><div class="item-desc">Grilled Capsicum &amp; Onion, Salsa, Guacamole &amp; Sour Cream</div></div>
    <div class="item"><div class="item-name">California</div><div class="item-desc">Fries, Cheese, Salsa, Guacamole &amp; Sour Cream</div></div>

    <div class="step"><span class="step-label">Step Two</span><span class="step-title">Choose your filling</span></div>
    <div class="leader"><span class="item-name">Mexican Chicken</span><span class="dots"></span><span class="value">Marinated Breast Chicken</span></div>
    <div class="leader"><span class="item-name">Chipotle Steak</span><span class="dots"></span><span class="value">Juicy Chargrilled Steak</span></div>
    <div class="leader"><span class="item-name">Fish Fillet</span><span class="dots"></span><span class="value">Flash Fried</span></div>
    <div class="leader"><span class="item-name">Salute Prawn</span><span class="dots"></span><span class="value">With Lemon &amp; Herb</span></div>
    <div class="fillings-art">
      <div class="sketch" role="img" aria-label="Sketch of chicken breast"></div>
      <div class="sketch" role="img" aria-label="Sketch of steak"></div>
      <div class="sketch" role="img" aria-label="Sketch of fish fillet"></div>
      <div class="sketch" role="img" aria-label="Sketch of prawn"></div>
    </div>

    <div class="step"><span class="step-label">Step Three</span><span class="step-title">Add a sauce (optional)</span></div>
    <div class="leader"><span class="item-name">Corriander &amp; Lime</span><span class="dots"></span><span class="heat heat--mild">(MILD)</span></div>
    <div class="leader"><span class="item-name">Chipotle</span><span class="dots"></span><span class="heat heat--medium">(MEDIUM)</span></div>
    <div class="leader"><span class="item-name">Hot Sauce</span><span class="dots"></span><span class="heat heat--hot">(HOT)</span></div>
    <div class="leader"><span class="item-name">Habannero</span><span class="dots"></span><span class="heat heat--insane">(INSANE)</span></div>
    <div class="spacer"></div>
    <div class="leader"><span class="item-name">Extras</span><span class="dots"></span><span class="value">$1</span></div>
    <div class="leader"><span class="item-name">Guacamole</span><span class="dots"></span><span class="value">$2</span></div>
    <div class="leader"><span class="item-name">Extra Filling</span><span class="dots"></span><span class="value">$3</span></div>

    <div class="meal">
      <div><h3 class="section-title">Make it a meal</h3><p class="meal-desc">Fries, Sauce and a Drink</p></div>
      <div class="sketch" style="width:70px;height:62px" role="img" aria-label="Sketch of drink and fries"></div>
      <div class="tag"><svg viewBox="0 0 100 50" preserveAspectRatio="none"><path d="M3 25 L20 4 H97 V46 H20 Z" fill="#fff" stroke="#1e1e1e" stroke-width="2.5"/><circle cx="16" cy="25" r="3" fill="none" stroke="#1e1e1e" stroke-width="2"/></svg><span>$4.50</span></div>
    </div>
  </section>

  <!-- Burgers -->
  <section class="panel panel--middle">
    <div class="head-row">
      <div>
        <h2 class="section-title">Burgers</h2>
        <p class="tagline">Out of this world! A good<br>burger is a messy burger!</p>
      </div>
      <div class="sketch" style="width:74px;height:70px" role="img" aria-label="Hand-drawn sketch of a burger"></div>
      <div class="tag"><svg viewBox="0 0 100 50" preserveAspectRatio="none"><path d="M3 25 L20 4 H97 V46 H20 Z" fill="#fff" stroke="#1e1e1e" stroke-width="2.5"/><circle cx="16" cy="25" r="3" fill="none" stroke="#1e1e1e" stroke-width="2"/></svg><span>$9</span></div>
    </div>

    <div class="head-row" style="margin-top:18px">
      <div><h3 class="section-title">Beef</h3><p class="item-desc" style="font-size:16px">200 gram! You got beef wid dat?</p></div>
      <div class="sketch" style="width:58px;height:42px;margin-right:40px" role="img" aria-label="Sketch of a beef patty"></div>
    </div>
    <div style="margin-top:8px">
      <div class="item"><div class="item-name">Classic Beef</div><div class="item-desc">Lettuce, Tomato, Grilled Onion, BBQ Sauce</div></div>
      <div class="item"><div class="item-name">Aussie Burger</div><div class="item-desc">Lettuce, Tomato, Grilled Onion, Pineapple, Beef Rashes, BBQ Sauce</div></div>
      <div class="item"><div class="item-name">American</div><div class="item-desc">Coleslaw, Tomato, Fries, Pickles, Mayo, Ketchup</div></div>
      <div class="item"><div class="item-name">Cheese Burger</div><div class="item-desc">Cheese, Pickles, Onion, Mustard, Ketchup, Mayo</div></div>
      <div class="item"><div class="item-name">Backyard Burger</div><div class="item-desc">Lettuce, Tomato, Cheese, Pickles, Onion, Mustard, Ketchup, Mayo</div></div>
      <div class="item"><div class="item-name">Surf 'n' Turf</div><div class="item-desc">Lettuce, Tomato, Calamari, Harrissa Paste, Ketchup, Mayo</div></div>
    </div>

    <div class="head-row" style="margin-top:14px">
      <div><h3 class="section-title">Chicken</h3><p class="item-desc" style="font-size:16px">Mmm chiiigen...</p></div>
      <div class="sketch" style="width:80px;height:58px;margin-right:40px" role="img" aria-label="Sketch of a chicken drumstick"></div>
    </div>
    <div style="margin-top:8px">
      <div class="item"><div class="item-name">Classic Chicken</div><div class="item-desc">Crispy Chicken Tenders, Lettuce, Cheese, Feisty Mayo</div></div>
      <div class="item"><div class="item-name">Chicken 'n' Chips</div><div class="item-desc">Crispy Chicken Tenders, Fries, Coleslaw, Cheese, Feisty Mayo</div></div>
      <div class="item"><div class="item-name">Mexican</div><div class="item-desc">Grilled Chicken Breast, Lettuce, Salsa, Guacamole, Southwest Sauce</div></div>
      <div class="item"><div class="item-name">Portuguese</div><div class="item-desc">Grilled Chicken Breast, Lettuce, Cheese, Mayo, Peri Peri</div></div>
      <div class="item"><div class="item-name">Lebanese</div><div class="item-desc">Grilled Chicken Breast, Fries, Lebanese Pickles, Garlic Sauce</div></div>
    </div>

    <div class="spacer"></div>
    <div class="leader" style="margin-bottom:4px"><span class="item-name">Extras</span><span class="dots"></span><span class="value">$1</span></div>
    <div class="leader" style="margin-bottom:4px"><span class="item-name">Guacamole</span><span class="dots"></span><span class="value">$2</span></div>
    <div class="leader" style="margin-bottom:0"><span class="item-name">Double Beef or Chicken</span><span class="dots"></span><span class="value">$3</span></div>
    <p class="item-desc">(Make sure you're hungry!)</p>

    <div class="meal">
      <div><h3 class="section-title">Make it a meal</h3><p class="meal-desc">Fries, Sauce and a Drink</p></div>
      <div class="sketch" style="width:70px;height:62px" role="img" aria-label="Sketch of drink and fries"></div>
      <div class="tag"><svg viewBox="0 0 100 50" preserveAspectRatio="none"><path d="M3 25 L20 4 H97 V46 H20 Z" fill="#fff" stroke="#1e1e1e" stroke-width="2.5"/><circle cx="16" cy="25" r="3" fill="none" stroke="#1e1e1e" stroke-width="2"/></svg><span>$4.50</span></div>
    </div>
  </section>

  <!-- Ribs, nachos, waffles -->
  <section class="panel panel--right">
    <h2 class="section-title">Buffalo Chicken Ribs</h2>
    <p class="tagline" style="font-size:16px">Is when a buffalo makes love to a chicken...<br>drenched in sauce and served with ranch.</p>

    <div class="head-row" style="margin-top:14px">
      <div><h3 class="section-title" style="font-size:17px">Sauces</h3><p class="item-desc">Lemon &amp; Herb, BBQ, Hot Sauce, Peri Peri</p></div>
      <div class="sketch" style="width:34px;height:26px;margin-right:34px" role="img" aria-label="Sketch of a sauce cup"></div>
    </div>
    <div class="price-row">
      <div class="pack" style="margin-top:14px">6 Pack<div class="tag tag--small"><svg viewBox="0 0 100 50" preserveAspectRatio="none"><path d="M3 25 L20 4 H97 V46 H20 Z" fill="#fff" stroke="#1e1e1e" stroke-width="2.5"/><circle cx="16" cy="25" r="3" fill="none" stroke="#1e1e1e" stroke-width="2"/></svg><span>$4.95</span></div></div>
      <div class="pack" style="margin-top:4px">12 Pack<div class="tag tag--small"><svg viewBox="0 0 100 50" preserveAspectRatio="none"><path d="M3 25 L20 4 H97 V46 H20 Z" fill="#fff" stroke="#1e1e1e" stroke-width="2.5"/><circle cx="16" cy="25" r="3" fill="none" stroke="#1e1e1e" stroke-width="2"/></svg><span>$14.95</span></div></div>
      <div class="pack">24 Pack<div class="tag tag--small"><svg viewBox="0 0 100 50" preserveAspectRatio="none"><path d="M3 25 L20 4 H97 V46 H20 Z" fill="#fff" stroke="#1e1e1e" stroke-width="2.5"/><circle cx="16" cy="25" r="3" fill="none" stroke="#1e1e1e" stroke-width="2"/></svg><span>$7.95</span></div></div>
    </div>

    <div class="head-row">
      <div><h3 class="section-title" style="font-size:17px">Nachos</h3><p class="tagline" style="margin-top:2px;font-size:16px">Corn Chips 'n' Stuff</p></div>
      <div class="sketch" style="width:88px;height:56px;margin-right:40px" role="img" aria-label="Sketch of a plate of nachos with dip"></div>
    </div>
    <div class="head-row" style="margin-top:8px">
      <div class="item"><div class="item-name">Nachos Guacamole</div><div class="item-desc">Guacamole, Sour Cream &amp; Cheese</div></div>
      <div class="tag tag--small" style="margin-right:60px"><svg viewBox="0 0 100 50" preserveAspectRatio="none"><path d="M3 25 L20 4 H97 V46 H20 Z" fill="#fff" stroke="#1e1e1e" stroke-width="2.5"/><circle cx="16" cy="25" r="3" fill="none" stroke="#1e1e1e" stroke-width="2"/></svg><span>$7</span></div>
    </div>
    <div class="head-row">
      <div class="item"><div class="item-name">Nachos Beef</div><div class="item-desc">Corn Chips, Salsa, Beef Chilli,<br>Sour Cream &amp; Cheese</div></div>
      <div class="tag tag--small" style="margin-right:70px"><svg viewBox="0 0 100 50" preserveAspectRatio="none"><path d="M3 25 L20 4 H97 V46 H20 Z" fill="#fff" stroke="#1e1e1e" stroke-width="2.5"/><circle cx="16" cy="25" r="3" fill="none" stroke="#1e1e1e" stroke-width="2"/></svg><span>$7</span></div>
    </div>
    <div class="head-row" style="justify-content:flex-start;gap:14px">
      <div class="item"><div class="item-name">Macho Nachos</div><div class="item-desc">All of the above</div></div>
      <div class="tag tag--small"><svg viewBox="0 0 100 50" preserveAspectRatio="none"><path d="M3 25 L20 4 H97 V46 H20 Z" fill="#fff" stroke="#1e1e1e" stroke-width="2.5"/><circle cx="16" cy="25" r="3" fill="none" stroke="#1e1e1e" stroke-width="2"/></svg><span>$9</span></div>
    </div>
    <div class="head-row" style="margin-top:4px">
      <div style="display:flex;align-items:center;gap:10px">
        <h3 class="section-title" style="font-size:17px">Fries</h3>
        <div class="sketch" style="width:34px;height:40px" role="img" aria-label="Sketch of fries"></div>
        <div class="tag tag--small"><svg viewBox="0 0 100 50" preserveAspectRatio="none"><path d="M3 25 L20 4 H97 V46 H20 Z" fill="#fff" stroke="#1e1e1e" stroke-width="2.5"/><circle cx="16" cy="25" r="3" fill="none" stroke="#1e1e1e" stroke-width="2"/></svg><span>$4</span></div>
      </div>
      <div class="tag tag--small" style="transform:rotate(-35deg)"><svg viewBox="0 0 100 50" preserveAspectRatio="none"><path d="M3 25 L20 4 H97 V46 H20 Z" fill="#fff" stroke="#1e1e1e" stroke-width="2.5"/><circle cx="16" cy="25" r="3" fill="none" stroke="#1e1e1e" stroke-width="2"/></svg><span>$10</span></div>
    </div>

    <h3 class="section-title" style="font-size:17px;margin-top:4px">Belgian Waffles</h3>
    <p class="tagline" style="font-size:16px">(NOT FROZEN)</p>
    <p class="tagline" style="font-size:16px;margin-top:8px">House made waffles, freshly made while you wait!</p>
    <p class="item-desc" style="margin-top:6px">Served with fresh Strawberries, pure Canadian Maple Syrup, Belgian Chocolate and Fresh Cream. Enough said.</p>

    <div class="notice">
      <p>We source and use the best quality ingredients and serve it the freshest way possible.</p>
      <p>All menu items have been prepared with care and are cooked while you wait.</p>
      <p>Please be patient<br>as your food is being made.</p>
      <span class="chili chili--left" role="img" aria-label="Sketch of a chilli pepper"></span>
      <span class="chili chili--right" role="img" aria-label="Sketch of a chilli pepper"></span>
    </div>
  </section>

</main>
</body>
</html>
```